Window cover film/full size advertisement.

Our company specializes in custom woodworking and cabinetry. We produce high end, custom build units for kitchens, bars, bathroom vanities, TV units, etc... Looking to have a design made to be printed on a perforated film to be placed on our office windows. The window placement and sizes can be found in the file attached. The best design must have pictures and logo as well as clearly visible phone number and website address. We are looking to cover 6 windows in the frond ( under the sigh) and 6 windows on the side of the building.

Tv

• should not have a lot of empty/white space on the design.

```html
<!DOCTYPE html>
<html lang="en">
<head>
<meta charset="utf-8">
<title>Maplecrest Interiors – Window Film Concepts</title>
<link href="https://fonts.googleapis.com/css2?family=Roboto+Condensed:wght@300;400;700&display=swap" rel="stylesheet">
<style>
  :root {
    --board: #1d1d1d;
    --label: #a9a9a9;
    --blue: #2456a8;
    --blue-light: #3a7bd0;
    --blue-deep: #1b3f8c;
    --green: #6cbd45;
    --green-dark: #4f9a2e;
    --title-blue: #1f4fa3;
    --white: #ffffff;
    --caption-bg: rgba(58, 42, 32, 0.92);
  }
  * { margin: 0; padding: 0; box-sizing: border-box; }
  html, body { width: 1200px; height: 1000px; overflow: hidden; }
  body {
    background: var(--board);
    font-family: "Roboto Condensed", "Arial Narrow", sans-serif;
    position: relative;
  }
  .concept-label {
    position: absolute;
    top: 132px;
    width: 484px;
    text-align: center;
    color: var(--label);
    font-weight: 300;
    font-size: 38px;
  }
  .window-film {
    position: absolute;
    width: 484px;
    height: 537px;
    overflow: hidden;
    background: var(--blue);
  }
  .film-art { position: absolute; inset: 0; width: 100%; height: 100%; }
  .services {
    position: absolute;
    left: 11px;
    top: 14px;
  }
  .services h2 {
    color: var(--title-blue);
    font-weight: 700;
    font-size: 17px;
    margin-bottom: 7px;
  }
  .services ul { list-style: none; }
  .services li {
    color: var(--green-dark);
    font-weight: 700;
    font-size: 12px;
    line-height: 20px;
    display: flex;
    align-items: center;
    gap: 7px;
  }
  .services li svg { width: 9px; height: 9px; }
  .brand {
    position: absolute;
    right: 12px;
    top: 12px;
    display: flex;
    flex-direction: column;
    align-items: flex-end;
    gap: 8px;
  }
  .brand-square {
    width: 60px;
    height: 60px;
    border: 3px solid var(--white);
    margin-right: 32px;
  }
  .brand-name {
    color: var(--white);
    font-weight: 400;
    font-size: 22px;
  }
  .showroom-note {
    position: absolute;
    left: 10px;
    top: 462px;
    width: 266px;
    padding: 5px 10px 6px;
    background: var(--caption-bg);
    color: var(--white);
    border-radius: 2px;
  }
  .showroom-note strong { display: block; font-weight: 400; font-size: 16px; line-height: 18px; }
  .showroom-note span { display: block; font-weight: 400; font-size: 10px; line-height: 13px; }
  .contact {
    position: absolute;
    left: 281px;
    top: 436px;
    width: 188px;
    color: var(--white);
    text-align: right;
  }
  .contact .phone {
    font-weight: 300;
    font-size: 30px;
    line-height: 36px;
    border-bottom: 1px dashed rgba(255,255,255,0.8);
    padding-bottom: 3px;
    margin-bottom: 3px;
  }
  .contact .line { font-weight: 400; font-size: 15px; line-height: 19px; }
</style>
</head>
<body>

<p class="concept-label" style="left:88px;">sample 1</p>
<p class="concept-label" style="left:624px;">sample 2</p>

<!-- Concept one -->
<section class="window-film" style="left:88px; top:249px;">
  <svg class="film-art" viewBox="0 0 484 537" preserveAspectRatio="none">
    <defs>
      <radialGradient id="blueGlowA" cx="0.75" cy="0.3" r="0.8">
        <stop offset="0" stop-color="#3f86d8"/>
        <stop offset="0.6" stop-color="#2556aa"/>
        <stop offset="1" stop-color="#1c428f"/>
      </radialGradient>
      <linearGradient id="kitchenLight" x1="0" y1="0" x2="0" y2="1">
        <stop offset="0" stop-color="#f4f3f0"/>
        <stop offset="0.35" stop-color="#e7e2da"/>
        <stop offset="0.62" stop-color="#8a6c55"/>
        <stop offset="1" stop-color="#b8946c"/>
      </linearGradient>
    </defs>
    <rect width="484" height="537" fill="url(#blueGlowA)"/>
    <path d="M400,0 C470,120 470,260 420,380" fill="none" stroke="#4a8fe0" stroke-width="2" opacity="0.35"/>
    <path role="img" aria-label="Photo of a bright modern kitchen with dark wood cabinets, white island and light wood floor"
          d="M0,0 L245,0 C360,80 405,270 360,420 C330,490 240,528 150,537 L0,537 Z" fill="url(#kitchenLight)"/>
    <path d="M245,0 C385,90 425,300 335,470 C300,515 230,532 185,537 L135,537 C245,520 340,470 368,380 C405,250 365,85 245,0 Z" fill="var(--green)"/>
    <path d="M330,430 C360,470 360,500 300,537 L280,537 C330,500 340,470 330,430 Z" fill="var(--green)"/>
  </svg>

  <div class="services">
    <h2>We Specialize in</h2>
    <ul>
      <li><svg viewBox="0 0 10 10"><path d="M1,5 L4,8 L9,1" fill="none" stroke="#4f9a2e" stroke-width="2"/></svg>Kitchens</li>
      <li><svg viewBox="0 0 10 10"><path d="M1,5 L4,8 L9,1" fill="none" stroke="#4f9a2e" stroke-width="2"/></svg>Bars</li>
      <li><svg viewBox="0 0 10 10"><path d="M1,5 L4,8 L9,1" fill="none" stroke="#4f9a2e" stroke-width="2"/></svg>Bathroom vanities</li>
      <li><svg viewBox="0 0 10 10"><path d="M1,5 L4,8 L9,1" fill="none" stroke="#4f9a2e" stroke-width="2"/></svg>Custom closets</li>
      <li><svg viewBox="0 0 10 10"><path d="M1,5 L4,8 L9,1" fill="none" stroke="#4f9a2e" stroke-width="2"/></svg>TV Units</li>
    </ul>
  </div>

  <div class="brand">
    <div class="brand-square"></div>
    <div class="brand-name">Maplecrest Interiors</div>
  </div>

  <div class="showroom-note">
    <strong>We have a showroom upstairs.</strong>
    <span>Looking forward to seeing more from you.</span>
  </div>

  <div class="contact">
    <div class="phone">(555).010.4827</div>
    <div class="line">info@maplecrestinteriors.ca</div>
    <div class="line">www.maplecrestinteriors.ca</div>
  </div>
</section>

<!-- Concept two -->
<section class="window-film" style="left:624px; top:250px;">
  <svg class="film-art" viewBox="0 0 484 537" preserveAspectRatio="none">
    <defs>
      <radialGradient id="blueGlowB" cx="0.75" cy="0.3" r="0.8">
        <stop offset="0" stop-color="#3f86d8"/>
        <stop offset="0.6" stop-color="#2556aa"/>
        <stop offset="1" stop-color="#1c428f"/>
      </radialGradient>
      <linearGradient id="kitchenDark" x1="0" y1="0" x2="0" y2="1">
        <stop offset="0" stop-color="#eeede9"/>
        <stop offset="0.3" stop-color="#8a8884"/>
        <stop offset="0.55" stop-color="#3e3a36"/>
        <stop offset="0.8" stop-color="#6a4a32"/>
        <stop offset="1" stop-color="#c9c2b6"/>
      </linearGradient>
    </defs>
    <rect width="484" height="537" fill="url(#blueGlowB)"/>
    <path d="M400,0 C470,120 470,260 420,380" fill="none" stroke="#4a8fe0" stroke-width="2" opacity="0.35"/>
    <path role="img" aria-label="Photo of a contemporary kitchen with grey cabinets, round pendant lights and a wooden dining table with chairs"
          d="M0,0 L245,0 C360,80 405,270 360,420 C330,490 240,528 150,537 L0,537 Z" fill="url(#kitchenDark)"/>
    <path d="M245,0 C385,90 425,300 335,470 C300,515 230,532 185,537 L135,537 C245,520 340,470 368,380 C405,250 365,85 245,0 Z" fill="var(--green)"/>
    <path d="M330,430 C360,470 360,500 300,537 L280,537 C330,500 340,470 330,430 Z" fill="var(--green)"/>
  </svg>

  <div class="services">
    <h2>We Specialize in</h2>
    <ul>
      <li><svg viewBox="0 0 10 10"><path d="M1,5 L4,8 L9,1" fill="none" stroke="#4f9a2e" stroke-width="2"/></svg>Kitchens</li>
      <li><svg viewBox="0 0 10 10"><path d="M1,5 L4,8 L9,1" fill="none" stroke="#4f9a2e" stroke-width="2"/></svg>Bars</li>
      <li><svg viewBox="0 0 10 10"><path d="M1,5 L4,8 L9,1" fill="none" stroke="#4f9a2e" stroke-width="2"/></svg>Bathroom vanities</li>
      <li><svg viewBox="0 0 10 10"><path d="M1,5 L4,8 L9,1" fill="none" stroke="#4f9a2e" stroke-width="2"/></svg>Custom closets</li>
      <li><svg viewBox="0 0 10 10"><path d="M1,5 L4,8 L9,1" fill="none" stroke="#4f9a2e" stroke-width="2"/></svg>TV Units</li>
    </ul>
  </div>

  <div class="brand">
    <div class="brand-square"></div>
    <div class="brand-name">Maplecrest Interiors</div>
  </div>

  <div class="showroom-note">
    <strong>We have a showroom upstairs.</strong>
    <span>Looking forward to seeing more from you.</span>
  </div>

  <div class="contact">
    <div class="phone">(555).010.4827</div>
    <div class="line">info@maplecrestinteriors.ca</div>
    <div class="line">www.maplecrestinteriors.ca</div>
  </div>
</section>

</body>
</html>
```